Flyer für Selbstwert-Coachin und Bewusstseinstrainerin
Der Flyer ist wunderschön, kreativ und edel geworden und wurde von der Designerin genau nach meinen Wünschen super umgesetzt! Ich bin sehr zufrieden und kann die Designerin Lunea2281 jedem nur empfehlen. Einfach Top!!! 1 A!!! Vielen herzlichen Dank!
Zielgruppe
Ich bin Selbstwert Coach und Bewusstseinstrainerin und möchte einen Flyer für mein neues Angebot 'Innenkraft Akademie für Jugendliche ab 16' gestalten lassen.
Die Zielgruppe sind Eltern von Jugendlichen in der Oberstufe, deren Kinder unter Schulstress und Leistungsdruck leiden und zu wenig Selbstbewusstsein haben.
Aufgabenstellung
Ich habe bereits das Titelbild bei Bildquell gesucht #739201584, bitte dieses nehmen, es kann auch ein ähnliches noch besseres vorgeschlagen werden.
Ich möchte einen ansprechenden, schönen, hochwertigen Flyer mit den Farben der Landingpage, gelb, blau, gold... und Bilder von Jugendlichen, dort wo Platz ist, ansprechend und klar. Bitte keine Schnörkel und 08 15 Figuren, das Auge soll hängen bleiben, der Flyer hängt straßenseitig. Dieser soll ein 6-seitiger Wickelfalz sein.

```html
<!DOCTYPE html>
<html lang="de">
<head>
<meta charset="utf-8">
<title>Innenkraft Akademie – Flyer</title>
<link href="https://fonts.googleapis.com/css2?family=Oswald:wght@500&family=Open+Sans:ital,wght@0,400;0,700;1,400&display=swap" rel="stylesheet">
<style>
:root{
  --navy:#0c0a6b;
  --gold:#f6c400;
  --paper:#ffffff;
  --stage:#ebebeb;
  --frame:#d2d2d2;
  --ink:#2c2c2c;
}
*{box-sizing:border-box;margin:0;padding:0}
html,body{width:847px;height:1200px;overflow:hidden;background:var(--stage)}
body{font-family:"Open Sans",Arial,sans-serif;color:var(--ink);position:relative}
.row{position:absolute;left:74px;width:700px;height:502px;display:flex;border:1px solid var(--frame);background:var(--paper)}
.row-outside{top:96px}
.row-inside{top:607px}
.panel{position:relative;width:233.3px;height:100%;border-right:1px solid var(--frame);overflow:hidden}
.panel:last-child{border-right:0}
.photo{position:absolute;left:0;top:0;width:100%}
.photo-friends{height:158px;background:linear-gradient(135deg,#6d7a55,#c89b78 45%,#8a5b4a 70%,#3c3f52)}
.photo-books{height:128px;background:linear-gradient(160deg,#f3f3f1,#dcdcd8 60%,#7a9a4a)}
.photo-coach{height:155px;background:linear-gradient(120deg,#b5162a,#d9805f 45%,#e6b290 60%,#3f6b3a)}
.photo-cheer{height:132px;background:linear-gradient(135deg,#e8e6e2,#c9b8a6 45%,#5a4c6e 65%,#f0efec)}
.photo-study{height:202px;background:linear-gradient(140deg,#9db0a5,#5e7666 40%,#2f3b33 70%,#dedcd4)}
.photo-portrait{position:absolute;left:48px;top:190px;width:140px;height:200px;border-radius:46% 46% 40% 40%;background:linear-gradient(160deg,#c8582a,#e7b48f 50%,#2bb7a8)}
.band{position:absolute;left:0;display:flex;align-items:center;padding-left:9px;background:linear-gradient(90deg,var(--navy) 55%,rgba(12,10,107,0))}
.band h2{font-family:"Oswald",Arial Narrow,sans-serif;font-weight:500;font-size:15.5px;line-height:1.05;color:var(--gold);letter-spacing:.3px;text-transform:uppercase}
.band small{font-family:"Open Sans",sans-serif;font-size:7px;text-transform:none;letter-spacing:0}
.band-modules{top:128px;height:30px;width:210px}
.band-modules h2{font-size:20px}
.band-coach{top:140px;height:46px;width:200px}
.band-contact{top:18px;height:50px;width:190px}
.band-academy{top:205px;height:48px;width:233px}
.headline{font-family:"Oswald",Arial Narrow,sans-serif;font-weight:500;color:var(--navy);text-transform:uppercase;line-height:1.15}
.copy{position:absolute;left:12px;right:10px;font-size:6.9px;line-height:1.42}
.copy p{margin-bottom:6px}
.copy h3{font-size:10px;color:var(--navy);margin:5px 0 3px;font-weight:700}
.copy h4{font-size:6.9px;font-weight:700;margin-top:4px}
.copy ul{list-style:none;margin-bottom:2px}
.copy li{padding-left:9px;position:relative}
.copy li::before{content:"•";position:absolute;left:2px}
.gold-foot{position:absolute;left:0;bottom:0;width:100%;height:8px;background:linear-gradient(90deg,var(--gold),rgba(246,196,0,.15))}
.venue{position:absolute;left:6px;right:6px;top:440px;height:54px;border:2px solid var(--navy);border-radius:10px;text-align:center}
.venue h3{position:absolute;left:50%;top:-13px;transform:translateX(-50%);background:var(--paper);padding:0 10px;font-family:"Oswald",sans-serif;font-weight:500;font-size:18px;color:var(--navy)}
.venue p{margin-top:22px;font-size:7px;color:var(--navy)}
.benefits{list-style:none}
.benefits li{display:flex;gap:4px;font-size:7.4px;line-height:1.4;margin-bottom:5px}
.benefits svg{flex:none;margin-top:1px}
.contact-name{position:absolute;left:14px;top:86px;color:var(--navy)}
.contact-name strong{font-size:12.5px;display:block}
.contact-name span{font-size:7.6px}
.contact-lines{position:absolute;left:14px;top:133px;font-size:7.6px;color:var(--navy);line-height:1.5}
.brand{position:absolute;left:0;width:100%;top:428px;text-align:center;font-size:10px;color:#9b7a3e;display:flex;justify-content:center;align-items:center;gap:6px}
.brand i{width:8px;height:8px;border-radius:50%;background:#9b7a3e;display:inline-block}
.academy-copy{position:absolute;left:18px;right:10px;top:282px;font-size:8.4px;line-height:1.45;color:#333}
.academy-copy p{margin-bottom:11px}
.gold-strip{position:absolute;left:0;width:100%;background:linear-gradient(90deg,var(--gold),rgba(246,196,0,.2))}
.tagline{position:absolute;left:0;bottom:0;width:100%;height:50px;background:var(--navy);color:#fff;font-style:italic;font-size:8px;line-height:1.4;padding:6px 14px}
</style>
</head>
<body>

<section class="row row-outside">
  <article class="panel">
    <div class="photo photo-friends" role="img" aria-label="Foto: lachende Gruppe Jugendlicher im Freien"></div>
    <h2 class="headline" style="position:absolute;left:12px;top:176px;font-size:12px">Hast du das Gefühl, deinem Kind wird<br>alles zu viel?</h2>
    <div class="copy" style="top:222px">
      <p>Leidet auch dein Kind an Schulstress, Leistungsdruck und hat zu wenig Selbstbewusstsein?</p>
      <p>Das Jugendalter ist eine wichtige, oft schwierig verlaufende Entwicklungsphase, in der sich Jugendliche selbst erfahren und finden dürfen. Durch den stressigen, durch Leistungsdruck geprägten Schulalltag wird die Psyche doppelt gefordert. Viele Jugendliche fühlen sich schlecht, wissen oft nicht mehr weiter, negative Gedanken und Ängste machen sich breit. Oft geht der Glaube an sich selbst verloren. Das Selbstbewusstsein und der eigene Selbstwert schwinden.</p>
      <p>Ziel des begleitenden Coachings ist, die Jugendlichen zu befähigen, Herausforderungen des Lebens gut meistern und wieder Freude und Spaß am Leben empfinden zu können. Zu den Schwerpunkten zählt die Rückbesinnung auf sich selbst und die eigene Gefühlswelt, Persönlichkeitsentwicklung und die Anwendung der geistigen Gesetze.</p>
      <p>Der Lehrgang ist aktive Lebensschule, motiviert zur Freude an der Eigenverantwortung und Gestaltung eines glücklichen Lebens in körperlicher, geistiger und seelischer Gesundheit.</p>
    </div>
  </article>

  <article class="panel">
    <div class="photo photo-books" role="img" aria-label="Foto: Bücherstapel mit grünem Zweig"></div>
    <div class="band band-modules"><h2>20 Module</h2></div>
    <div class="copy" style="top:164px">
      <p><strong>Innerhalb von 20 Modulen während des Schuljahres</strong> werden einfache Übungen, Techniken und Methoden für den Alltag und die geistigen Lebensgesetze gelehrt und trainiert. Gemeinsam greifen wir Schwierigkeiten des täglichen Lebens auf und erarbeiten Lösungsmöglichkeiten.</p>
      <h3>INHALTE</h3>
      <h4>sich gut fühlen Dein Kind lernt,</h4>
      <ul>
        <li>mit negativen Gedanken und Gefühlen umzugehen</li>
        <li>aus sich selbst Kraft und Energie zu tanken</li>
        <li>trotz Schulstress und Belastungen entspannt zu bleiben</li>
        <li>angstfreier und gelassener zu sein</li>
      </ul>
      <h4>glücklich sein Dein Kind lernt,</h4>
      <ul>
        <li>mit mentalen Bildern und Affirmationen zu arbeiten</li>
        <li>auf seine innere Stimme und sein Herz zu hören und zu vertrauen</li>
        <li>sein Leben glücklich und erfolgreich zu gestalten und zu erleben</li>
      </ul>
      <h4>an sich glauben Dein Kind lernt,</h4>
      <ul>
        <li>an sich und seine Fähigkeiten zu glauben und ein positives Bild von sich zu entwickeln</li>
        <li>selbstsicher, selbstbewusst und innerlich stark zu werden</li>
        <li>sich zu vertrauen und sich zutrauen, das zu sagen, was es denkt und fühlt, egal was Mitschüler/innen oder Freund/innen denken</li>
        <li>sich selbst zu mögen und sich so anzunehmen, wie es ist</li>
        <li>mit Konflikten umzugehen und Probleme schneller zu lösen</li>
      </ul>
    </div>
    <div class="gold-foot"></div>
  </article>

  <article class="panel">
    <div class="photo photo-coach" role="img" aria-label="Foto: Porträt der Coachin vor roten Rosen"></div>
    <div class="band band-coach"><h2>Die Coachin und<br>Vortragende</h2></div>
    <div class="copy" style="top:196px">
      <p><strong>Clara Weidinger</strong> leitet den schulbegleitenden Lehrgang Innenkraft Akademie. Sie ist gelernte Pädagogin für allgemeinbildende höhere Schulen für die Fächer Psychologie/Philosophie/Pädagogik und Bildnerische Erziehung. Als Selbstwert- und Selbstbewusstseins Coach, Mental- und Emotional Coach und Bewusstseinstrainerin begleitet sie seit 2006 Erwachsene und Jugendliche in ihrer Praxis sowie online.</p>
      <p>Sie zeigt Wege aus Krisen und vermittelt Tools und Werkzeug, das „Wie“ um das eigene Leben glücklich gestalten zu können</p>
      <h3>TERMINE</h3>
      <p>Die 20 Module finden alle 2 Wochen immer dienstags (18.00 – ca. 20.00 Uhr oder länger) schulbegleitend statt und können nur insgesamt gebucht werden. (Terminänderungen vorbehalten)Die aktuellen Termine und Kosten für den gesamten Lehrgang finden Sie unter:<br><strong>https://www.innenkraft-staerken.at/innenkraft-akademie/</strong></p>
    </div>
    <div class="venue"><h3>ORT</h3><p>Der Lehrgang findet online via Konferio statt.</p></div>
  </article>
</section>

<section class="row row-inside">
  <article class="panel">
    <div class="photo photo-cheer" role="img" aria-label="Foto: jubelnde Jugendliche am Schreibtisch"></div>
    <h2 class="headline" style="position:absolute;left:12px;top:140px;font-size:19px">Vorteile und Nutzen</h2>
    <ul class="benefits" style="position:absolute;left:12px;right:8px;top:170px">
      <li><svg width="9" height="8" viewBox="0 0 9 8"><path d="M1 4l2.5 3L8 1" fill="none" stroke="#0c0a6b" stroke-width="1.6"/></svg><span>Beste Prävention für die psychische Gesundheit, Steigerung des Wohlbefindens von Geist, Körper und Seele</span></li>
      <li><svg width="9" height="8" viewBox="0 0 9 8"><path d="M1 4l2.5 3L8 1" fill="none" stroke="#0c0a6b" stroke-width="1.6"/></svg><span>Konkrete Lösungsansätze bei auftretenden Konflikten, Schulproblemen und Mobbing</span></li>
      <li><svg width="9" height="8" viewBox="0 0 9 8"><path d="M1 4l2.5 3L8 1" fill="none" stroke="#0c0a6b" stroke-width="1.6"/></svg><span>Veränderter Umgang bzw. Reduktion von Überforderung, Leistungsdruck und Schulstress</span></li>
      <li><svg width="9" height="8" viewBox="0 0 9 8"><path d="M1 4l2.5 3L8 1" fill="none" stroke="#0c0a6b" stroke-width="1.6"/></svg><span>Persönlichkeitsentwicklung, Lernen fürs Leben</span></li>
      <li><svg width="9" height="8" viewBox="0 0 9 8"><path d="M1 4l2.5 3L8 1" fill="none" stroke="#0c0a6b" stroke-width="1.6"/></svg><span>Grundlagen zur Gestaltung eines glücklichen, erfolgreichen Lebens</span></li>
      <li><svg width="9" height="8" viewBox="0 0 9 8"><path d="M1 4l2.5 3L8 1" fill="none" stroke="#0c0a6b" stroke-width="1.6"/></svg><span>Stärkung von Selbstbewusstsein, Selbstvertrauen, Selbstliebe und Selbstwert</span></li>
    </ul>
    <h2 class="headline" style="position:absolute;left:12px;top:380px;font-size:15px">Voraussetzungen für<br>die Teilnahme</h2>
    <div class="copy" style="top:420px">
      <p>Das wichtigste ist, dass dein Kind am Lehrgang teilnehmen will.</p>
      <p>Interesse, Neugierde und vor allem die Bereitschaft zur aktiven Umsetzung der Inhalte sind notwendig, um gute Ergebnisse zu erzielen.</p>
    </div>
  </article>

  <article class="panel">
    <div class="band band-contact"><h2>Kontakt &amp;<br>Veranstalterin:</h2></div>
    <div class="contact-name"><strong>Mag. Clara Weidinger</strong><span>Selbstwert Coach, Bewusstseinstrainerin</span></div>
    <div class="contact-lines">
      <div><strong>E-Mail :</strong>&nbsp; info@innenkraft-staerken.at</div>
      <div><strong>Mobil&nbsp; :</strong>&nbsp; +43(0)650 482 7731</div>
    </div>
    <div class="photo-portrait" role="img" aria-label="Porträtfoto der Coachin"></div>
    <div class="brand"><i></i><span>Mag. Clara Weidinger</span></div>
    <div class="gold-foot"></div>
  </article>

  <article class="panel">
    <div class="photo photo-study" role="img" aria-label="Foto: lächelnder Jugendlicher schreibt im Freien"></div>
    <div class="band band-academy"><h2>Innenkraft<br>Akademie <small>für Jugendliche ab 16</small></h2></div>
    <div class="gold-strip" style="top:253px;height:18px"></div>
    <div class="academy-copy">
      <p>Schulbegleitender Praxis Lehrgang für mentale Stärke und Selbstbewusstsein</p>
      <p>Schulstress &amp; Leistungsdruck bewältigen Selbstsicherer, gelassener &amp; angstfrei werden</p>
      <p>und dabei<br>ein starkes Selbstwertgefühl aufbauen<br>und sich selbst vertrauen</p>
    </div>
    <div class="gold-strip" style="top:442px;height:10px"></div>
    <div class="tagline">Einfache Übungen, Techniken und Methoden für den Alltag und ein glückliches erfolgreiches Leben</div>
  </article>
</section>

</body>
</html>
```